Marketing Skill "Workouts"; Design for an e-mail attachment highlighting Marketing training subjects

I am a freelance marketing trainer based in Singapore and need to e-mail out an attachment (probably saved as a PDF) to potential clients showing the training services I offer. These clients are all large blue-chip multinational companies so the attachment needs to look professional/high quality when opened on a computer.

My Company is called "Brightline Marketing" (logo attached)

I am assuming the size should be A4 one sided colour.

I have attached some files that show best-attempts so far. These contain the key information, but the layouts all still look rather pedestrian. I am looking for something that looks a bit more dynamic but remains clear/easy to read.

Target Market(s)

HR/Marketing managers in multinational firms, mainly consumer goods

Industry/Entity Type

Marketing

Font styles to use
Sans Serif

Colors

Designer to choose colors to be used in the design.

Requirements
Must have
• Must look modern, up-to-date, professional.
Should not have
• Not gimmicky, like a cheap deal

```html
<!DOCTYPE html>
<html lang="en">
<head>
<meta charset="utf-8">
<title>Marketing Skill Workouts – Brightline Marketing</title>
<link rel="stylesheet" href="https://fonts.googleapis.com/css2?family=Lato:ital,wght@0,400;0,700;0,900;1,700;1,900&family=Oswald:wght@600;700&display=swap">
<style>
  :root {
    --red: #9e1409;
    --red-dark: #7a0f07;
    --red-bright: #c8241a;
    --ink: #2a2a2a;
    --white: #ffffff;
    --page-bg: #3b3b3c;
    --box-grey: #e4e4e4;
  }
  * { box-sizing: border-box; margin: 0; padding: 0; }
  html, body { width: 1200px; height: 1200px; overflow: hidden; }
  body { background: var(--page-bg); font-family: "Lato", Arial, sans-serif; color: var(--ink); position: relative; }

  .flyer { position: absolute; left: 178px; top: 56px; width: 842px; height: 1090px; background: var(--white); overflow: hidden; box-shadow: 0 6px 24px rgba(0,0,0,.45); }

  .header { position: absolute; inset: 0 0 auto 0; height: 134px; }
  .header-art { position: absolute; inset: 0; }
  .brand { position: absolute; left: 40px; top: 50px; display: flex; align-items: center; gap: 12px; }
  .brand-name { font-weight: 400; font-size: 31px; color: var(--ink); letter-spacing: .2px; }
  .brand-dot { width: 30px; height: 30px; border-radius: 50%; background: var(--red); }

  .contact { position: absolute; left: 520px; top: 24px; list-style: none; }
  .contact li { display: flex; align-items: center; gap: 8px; height: 29.5px; color: var(--white); font-weight: 700; font-size: 17px; white-space: nowrap; }
  .contact svg { width: 20px; height: 20px; flex: none; }

  .photos { position: absolute; left: 0; top: 134px; width: 842px; height: 180px; }

  .hero { position: absolute; left: 0; top: 316px; width: 842px; height: 184px; background: linear-gradient(90deg, var(--red-dark), var(--red) 50%, var(--red-dark)); color: var(--white); text-align: center; }
  .hero-title { font-family: "Oswald", Impact, sans-serif; font-weight: 700; font-size: 60px; line-height: 1; margin-top: 8px; letter-spacing: .5px; }
  .hero-question { font-weight: 900; font-size: 29px; line-height: 34px; margin-top: 10px; }
  .hero-copy { font-size: 20.5px; line-height: 26px; margin: 6px auto 0; max-width: 745px; }

  .section-title { display: flex; align-items: center; gap: 8px; font-family: "Oswald", Impact, sans-serif; font-weight: 700; font-size: 32px; color: var(--red); line-height: 1; }
  .section-title span { border-bottom: 2px solid var(--red); padding-bottom: 1px; }
  .section-title svg { width: 40px; height: 40px; }

  .topics { position: absolute; left: 22px; top: 510px; width: 412px; }
  .topic-list { list-style: none; margin-top: 8px; }
  .topic-list li { position: relative; padding-left: 46px; font-size: 18.5px; line-height: 23px; margin-bottom: 7.2px; letter-spacing: -.1px; }
  .topic-list li::before { content: ""; position: absolute; left: 16px; top: 5px; width: 13px; height: 13px; border-radius: 50%; background: var(--red-bright); box-shadow: 0 0 0 2px var(--white), 0 0 0 3.5px var(--red-bright); }

  .divider { position: absolute; left: 443px; top: 510px; width: 2px; height: 370px; background: linear-gradient(var(--white), #b9b9b9 20%, #b9b9b9 80%, var(--white)); }

  .benefits { position: absolute; left: 476px; top: 510px; width: 350px; }
  .benefit-list { list-style: none; }
  .benefit-list li { position: absolute; left: 0; display: flex; align-items: center; gap: 14px; font-size: 20px; line-height: 25px; white-space: nowrap; }
  .benefit-list svg { width: 42px; height: 42px; flex: none; }

  .why { position: absolute; left: 34px; top: 896px; width: 766px; height: 176px; border: 2px solid var(--red-bright); border-radius: 28px; padding: 8px; }
  .why-inner { width: 100%; height: 100%; border: 2px solid #2c2c2c; border-radius: 22px; background: linear-gradient(#f4f4f4, var(--box-grey) 60%, #d2d2d2); text-align: center; padding-top: 50px; }
  .why-copy { font-size: 16px; line-height: 20px; color: #1e1e1e; }
  .why-tagline { font-weight: 900; font-style: italic; font-size: 29px; line-height: 32px; color: var(--red-dark); margin-top: 4px; }
  .why-ribbon { position: absolute; left: 292px; top: -10px; width: 186px; height: 70px; }
  .why-ribbon-label { position: absolute; left: 0; right: 0; top: -2px; text-align: center; font-family: "Oswald", Impact, sans-serif; font-weight: 700; font-size: 35px; line-height: 50px; color: var(--white); }
</style>
</head>
<body>
<main class="flyer">

  <header class="header">
    <svg class="header-art" width="842" height="134" viewBox="0 0 842 134" aria-hidden="true">
      <defs>
        <linearGradient id="panelShade" x1="0" x2="1">
          <stop offset="0" stop-color="#3f4041"/>
          <stop offset="1" stop-color="#6a6b6c"/>
        </linearGradient>
      </defs>
      <polygon points="430,0 842,0 842,134 486,134" fill="url(#panelShade)"/>
      <polygon points="382,0 420,0 476,134 438,134" fill="var(--red)"/>
      <rect x="0" y="132" width="842" height="2" fill="var(--red)"/>
    </svg>
    <div class="brand">
      <span class="brand-name">Brightline Marketing</span>
      <span class="brand-dot"></span>
    </div>
    <ul class="contact">
      <li>
        <svg viewBox="0 0 20 20" aria-hidden="true"><circle cx="10" cy="10" r="9" fill="none" stroke="#fff" stroke-width="1.5"/><path d="M7 5.5l1.6 2.3-1 1.1c.7 1.4 1.6 2.3 3 3l1.1-1 2.3 1.6-.9 1.6c-3.4-.4-6.1-3.1-6.5-6.5z" fill="#fff"/></svg>
        +65 6100 4827
      </li>
      <li>
        <svg viewBox="0 0 20 20" aria-hidden="true"><circle cx="10" cy="10" r="9" fill="none" stroke="#fff" stroke-width="1.5"/><circle cx="10" cy="10" r="5.5" fill="none" stroke="#fff" stroke-width="1.2"/><path d="M4.5 10h11M10 4.5v11" stroke="#fff" stroke-width="1.2"/></svg>
        www.brightline-marketing.com
      </li>
      <li>
        <svg viewBox="0 0 20 20" aria-hidden="true"><circle cx="10" cy="10" r="9" fill="none" stroke="#fff" stroke-width="1.5"/><rect x="5" y="6.5" width="10" height="7" fill="none" stroke="#fff" stroke-width="1.3"/><path d="M5 6.5l5 4 5-4" fill="none" stroke="#fff" stroke-width="1.3"/></svg>
        alex@brightline-marketing.com
      </li>
    </ul>
  </header>

  <svg class="photos" width="842" height="180" viewBox="0 0 842 180">
    <defs>
      <linearGradient id="gymWarm" x1="0" y1="0" x2="0" y2="1">
        <stop offset="0" stop-color="#b9b3ab"/>
        <stop offset=".6" stop-color="#a58068"/>
        <stop offset="1" stop-color="#e08a3a"/>
      </linearGradient>
      <linearGradient id="gymCool" x1="0" y1="0" x2="1" y2="1">
        <stop offset="0" stop-color="#4d6f93"/>
        <stop offset=".55" stop-color="#3f7d8a"/>
        <stop offset="1" stop-color="#6b6f78"/>
      </linearGradient>
    </defs>
    <polygon role="img" aria-label="Photo: woman doing push-ups on an orange mat in a gym class" points="0,0 446,0 398,170 0,170" fill="url(#gymWarm)"/>
    <polygon role="img" aria-label="Photo: man lifting a barbell on a bench press" points="460,0 842,0 842,170 412,170" fill="url(#gymCool)"/>
    <rect x="0" y="175" width="842" height="3" fill="var(--red)"/>
  </svg>

  <section class="hero">
    <h1 class="hero-title">MARKETING SKILL 'WORKOUTS'</h1>
    <p class="hero-question">NO TIME TO LEARN?</p>
    <p class="hero-copy">Problem solved with 1 day intensive workshops that will drive business growth<br>and motivate your team.</p>
  </section>

  <section class="topics">
    <h2 class="section-title">
      <svg viewBox="0 0 40 40" aria-hidden="true"><path d="M6 20h22M22 12l8 8-8 8" fill="none" stroke="var(--red)" stroke-width="4" stroke-linecap="round" stroke-linejoin="round"/></svg>
      <span>Key Topics</span>
    </h2>
    <ul class="topic-list">
      <li>Developing strong brand plans</li>
      <li>Writing inspiring briefs/creative evaluation</li>
      <li>Shopper marketing/developing retail<br>promotions</li>
      <li>Brilliant launch management</li>
      <li>Improving marketing R.O.I.</li>
      <li>Driving brand growth without product<br>innovation</li>
      <li>Insight/concept development</li>
      <li>Integrating digital channels</li>
      <li>Creatvitiy and idea generation</li>
    </ul>
  </section>

  <div class="divider"></div>

  <section class="benefits">
    <h2 class="section-title">
      <svg viewBox="0 0 40 40" aria-hidden="true"><path d="M4 34l12-12 6 6 14-18" fill="none" stroke="var(--red)" stroke-width="4"/><path d="M28 8h9v9z" fill="var(--red)"/></svg>
      <span>Key Benefits</span>
    </h2>
    <ul class="benefit-list">
      <li style="top:52px">
        <svg viewBox="0 0 42 42" aria-hidden="true"><rect x="4" y="4" width="34" height="34" fill="none" stroke="var(--red)" stroke-width="3"/><rect x="10" y="24" width="5" height="10" fill="var(--red)"/><rect x="18" y="18" width="5" height="16" fill="var(--red)"/><rect x="26" y="12" width="5" height="22" fill="var(--red)"/></svg>
        <span>Latest in world-class<br>thinking/tools/case studies</span>
      </li>
      <li style="top:127px">
        <svg viewBox="0 0 42 42" aria-hidden="true"><rect x="3" y="12" width="36" height="24" rx="3" fill="none" stroke="var(--red)" stroke-width="3"/><path d="M15 12V7h12v5M3 22h36" fill="none" stroke="var(--red)" stroke-width="3"/><rect x="18" y="19" width="6" height="6" fill="var(--red)"/></svg>
        <span>Ability to 'customise' to address<br>your specific business issue</span>
      </li>
      <li style="top:197px">
        <svg viewBox="0 0 42 42" aria-hidden="true"><circle cx="21" cy="17" r="13" fill="none" stroke="var(--red)" stroke-width="2.5"/><path d="M8 17h26M21 4c-6 7-6 19 0 26M21 4c6 7 6 19 0 26" fill="none" stroke="var(--red)" stroke-width="2"/><path d="M21 30v6M13 38h16" stroke="var(--red)" stroke-width="3"/></svg>
        <span>Asian context/relevance</span>
      </li>
      <li style="top:259px">
        <svg viewBox="0 0 42 42" aria-hidden="true"><rect x="5" y="7" width="26" height="31" fill="none" stroke="var(--red)" stroke-width="3"/><path d="M11 4v6M18 4v6M25 4v6M10 18h12M10 25h10M10 32h8" stroke="var(--red)" stroke-width="2.5"/><path d="M38 12L24 30l-3 3 1-4 14-18z" fill="var(--red)"/></svg>
        <span>Take-away 'checklists' to embed<br>behaviours and skills</span>
      </li>
      <li style="top:333px">
        <svg viewBox="0 0 42 42" aria-hidden="true"><circle cx="21" cy="21" r="17" fill="none" stroke="var(--red)" stroke-width="2.5"/><path d="M13 21l6 6 11-12" fill="none" stroke="var(--red)" stroke-width="3" stroke-linecap="round" stroke-linejoin="round"/></svg>
        <span>Proven quality</span>
      </li>
    </ul>
  </section>

  <section class="why">
    <div class="why-inner">
      <p class="why-copy">The latest thinking, made practical and actionable.<br>20 years of business experience combined with over 10 years of proven training/facilitation for<br>major “blue-chip” clients, regularly scoring 90%+ satisfaction</p>
      <p class="why-tagline">World Class Quality without the costs</p>
    </div>
    <svg class="why-ribbon" viewBox="0 0 186 70" aria-hidden="true">
      <polygon points="0,6 16,0 170,0 186,6 172,6 172,42 93,70 14,42 14,6" fill="var(--red)"/>
      <polygon points="0,6 14,6 14,12" fill="var(--red-dark)"/>
      <polygon points="186,6 172,6 172,12" fill="var(--red-dark)"/>
    </svg>
    <div class="why-ribbon" style="height:auto"><div class="why-ribbon-label">Why Me?</div></div>
  </section>

</main>
</body>
</html>
```